Glow Up by Lakeside 21 day Challenge

We are having a Glow Up by Lakeside Challenge at our fitness studio. We need a poster design using the template attached as a reference. I have also included our Bromalux logo to put on the poster. Please DO NOT use the graphics in the flyer as we are expecting something much better :-)

-Size needed 11x17 with bleeding for printing

-We need this made in Photoshop (CS3 friendly) or at least delivered in PS as we might change some text or re-arrange the design later on.

-We need this in layers.

```html
<!DOCTYPE html>
<html lang="en">
<head>
<meta charset="utf-8">
<title>Glow Up by Lakeside 21 day Challenge – Bromalux</title>
<link rel="stylesheet" href="https://fonts.googleapis.com/css2?family=Rubik+Dirt&family=Sacramento&family=Arimo:wght@700&display=swap">
<style>
  :root {
    --paper: #ffffff;
    --orange: #f5a030;
    --lime: #b3c83a;
    --red: #c1202f;
    --pink: #e8197d;
    --yellow: #f8d42a;
    --teal: #5cbcbb;
    --ink: #454545;
    --ink-dark: #1e1e1e;
    --tulip-red: #e8322a;
    --stem-green: #6cc33a;
  }
  html, body {
    margin: 0;
    padding: 0;
    width: 796px;
    height: 1200px;
    overflow: hidden;
    background: var(--paper);
  }
  .poster {
    position: relative;
    width: 796px;
    height: 1200px;
    background: var(--paper);
    font-family: "Arimo", Arial, sans-serif;
    font-weight: 700;
  }
  .tulip-art {
    position: absolute;
    z-index: 0;
    left: 34px;
    top: 450px;
    width: 192px;
    height: 710px;
    border-radius: 96px 96px 16px 16px;
    background: linear-gradient(180deg, var(--tulip-red) 0%, var(--tulip-red) 26%, var(--stem-green) 40%, var(--stem-green) 100%);
  }
  .brand {
    position: absolute;
    z-index: 1;
    left: 255px;
    top: 118px;
    width: 288px;
    display: flex;
    align-items: center;
    justify-content: center;
    gap: 12px;
    font-family: "Rubik Dirt", system-ui, sans-serif;
    font-size: 44px;
    line-height: 1;
    color: var(--ink-dark);
  }
  .brand-mark {
    width: 18px;
    height: 18px;
    background: var(--ink-dark);
  }
  .headline {
    position: absolute;
    z-index: 1;
    left: 0;
    top: 0;
    width: 796px;
    height: 1200px;
    pointer-events: none;
  }
  .headline .display { font-family: "Rubik Dirt", system-ui, sans-serif; }
  .headline .script { font-family: "Sacramento", cursive; }
  .offer-list {
    position: absolute;
    z-index: 1;
    left: 240px;
    top: 752px;
    width: 412px;
    margin: 0;
    padding: 0;
    list-style: none;
    font-size: 15px;
    line-height: 18.5px;
    color: var(--ink);
  }
  .offer-list li {
    position: relative;
    padding-left: 32px;
  }
  .offer-list li::before {
    content: "";
    position: absolute;
    left: 2px;
    top: 7px;
    width: 7px;
    height: 7px;
    border-radius: 50%;
    background: var(--dot);
  }
  .offer-list .dot-pink { --dot: var(--pink); }
  .offer-list .dot-yellow { --dot: var(--yellow); }
  .offer-list .dot-teal { --dot: var(--teal); }
  .offer-list .dot-red { --dot: var(--red); }
  .offer-list .dot-yellow::before,
  .offer-list .dot-teal::before,
  .offer-list .dot-red::before { top: 16px; }
  .testimonial {
    position: absolute;
    z-index: 1;
    left: 242px;
    top: 988px;
    width: 505px;
    margin: 0;
    color: var(--ink);
  }
  .testimonial p {
    margin: 0;
    font-size: 19px;
  }
  .testimonial cite {
    display: block;
    text-align: right;
    font-style: normal;
    font-size: 13.5px;
    margin-top: 8px;
  }
  .urgency {
    position: absolute;
    z-index: 1;
    left: 242px;
    top: 1044px;
    margin: 0;
    font-size: 14px;
    line-height: 21px;
    color: var(--teal);
    text-transform: uppercase;
  }
</style>
</head>
<body>
<main class="poster">

  <div class="tulip-art" role="img" aria-label="Illustration of a single red tulip on a long green stem with leaves"></div>

  <div class="brand"><span class="brand-mark"></span>Bromalux</div>

  <svg class="headline" viewBox="0 0 796 1200" width="796" height="1200" aria-label="Glow Up by Lakeside Challenge">
    <text class="display" x="115" y="408" font-size="205" textLength="590" lengthAdjust="spacingAndGlyphs">
      <tspan fill="var(--orange)">G</tspan><tspan fill="var(--lime)">L</tspan><tspan fill="var(--red)">O</tspan><tspan fill="var(--pink)">W</tspan><tspan> </tspan><tspan fill="var(--yellow)">U</tspan><tspan fill="var(--teal)">P</tspan>
    </text>
    <text class="display" x="222" y="412" font-size="40" fill="var(--pink)">by</text>
    <text class="display" x="236" y="565" font-size="180" textLength="466" lengthAdjust="spacingAndGlyphs">
      <tspan fill="var(--yellow)">L</tspan><tspan fill="var(--teal)">A</tspan><tspan fill="var(--pink)">K</tspan><tspan fill="var(--lime)">E</tspan><tspan fill="var(--orange)">S</tspan><tspan fill="var(--teal)">I</tspan><tspan fill="var(--pink)">D</tspan><tspan fill="var(--lime)">E</tspan>
    </text>
    <text class="script" x="318" y="612" font-size="62" fill="none" stroke="var(--teal)" stroke-width="2">challenge</text>

    <text class="display" x="240" y="668" font-size="40" fill="var(--yellow)" textLength="478" lengthAdjust="spacingAndGlyphs">DISCOVER THE SECRET TO</text>
    <text class="display" x="240" y="708" font-size="40" fill="var(--lime)" textLength="400" lengthAdjust="spacingAndGlyphs">A BEACH-READY BODY</text>
    <text class="display" x="240" y="746" font-size="40" fill="var(--pink)" textLength="312" lengthAdjust="spacingAndGlyphs">IN JUST 21 DAYS!</text>

    <text class="display" x="240" y="932" font-size="36" fill="var(--orange)" textLength="467" lengthAdjust="spacingAndGlyphs">YOU GET ALL THIS-A $399 VALUE</text>
    <text class="display" x="240" y="974" font-size="46" fill="var(--pink)" textLength="272" lengthAdjust="spacingAndGlyphs">FOR ONLY $99!</text>
  </svg>

  <ul class="offer-list">
    <li class="dot-pink">9 total training sessions designed to incinerate fat off your midsection, thighs, and arms</li>
    <li class="dot-yellow">21 days of nutritional guidance, including delicious recipes</li>
    <li class="dot-teal">A Success Session to map out your individual plan for success</li>
    <li class="dot-red">Your very own Personal Accountability Coach to ensure you get results</li>
  </ul>

  <blockquote class="testimonial">
    <p>I've never been more fit in my life—at age 41!</p>
    <cite>~Marisol Penhale</cite>
  </blockquote>

  <p class="urgency">Hurry! Space is limited to only 20 participants!!!<br>Claim your spot now</p>

</main>
</body>
</html>
```